Detox Before & After Charts

I am looking to create a chart/graph to be used to chart a patient's progress before and after using our 15-day detox program. We will be looking for 3 different graphs to be made.
1. A chart showing the before and after symptom scores of 12 patients in a small clinical trial we did. We will use this one to show prospective patients.
2. A chart showing one single patient's "total" symptom scores before and after the detox. We will use this with each patient, before and after they do the detox.
3. A chart showing one patient's before and symptom scores in more detail, showing their scores in each one of the symptom categories. We will do this with each patient, before and after the detox.
For #2 & #3 above, we would want a master template that we could add the scoring for each new patient ourselves.
See attached for rough samples.
Each of these 3 charts should be the same style, but for now, just do chart #3. And after we decide on the designer, then we will have them do the other 2 charts.
And I prefer a line graph over a bar graph for these. I did not mention that at first. Sorry!!

```html
<!DOCTYPE html>
<html lang="en">
<head>
<meta charset="utf-8">
<title>Category Symptom Chart</title>
<link rel="stylesheet" href="https://fonts.googleapis.com/css2?family=Open+Sans:wght@300;400;600&family=Carlito:wght@400;700&display=swap">
<style>
  :root {
    --orange: #f07a0a;
    --yellow: #ffcc4d;
    --panel: #ececec;
    --field-border: #d6d6d6;
    --label: #8a8a8a;
    --before: #e3201f;
    --before-fill: #f3a59c;
    --before-text: #8b1a1a;
    --after: #4e8b2e;
    --after-fill: #a8d08d;
    --after-text: #375623;
    --after-green: #3fa535;
    --grid: #d9d9d9;
    --grid-minor: #efefef;
    --axis-text: #404040;
  }
  * { box-sizing: border-box; margin: 0; padding: 0; }
  html, body { width: 1200px; height: 848px; overflow: hidden; background: #fff; }
  body { position: relative; font-family: "Open Sans", Arial, sans-serif; }

  .band { position: absolute; left: 0; width: 1200px; }
  .band--top { top: 0; height: 38px; background: var(--orange); }
  .rule--top { top: 44px; height: 9px; background: var(--yellow); }
  .rule--bottom { top: 791px; height: 8px; background: var(--yellow); }
  .band--bottom { top: 806px; height: 42px; background: var(--orange); }

  .field-label { position: absolute; left: 46px; width: 84px; font-size: 14px; font-weight: 300; color: var(--label); }
  .field { position: absolute; left: 136px; width: 220px; height: 31px; border: 1px solid var(--field-border); border-radius: 4px; background: #fff; }

  .score-panel { position: absolute; left: 374px; top: 68px; width: 826px; height: 122px; background: var(--panel); border-radius: 14px 0 0 14px; }
  .date { position: absolute; font-size: 12px; font-weight: 600; color: #9a9a9a; transform: translateX(-50%); }
  .row-label { position: absolute; font-size: 14px; font-weight: 300; color: var(--label); text-align: right; }
  .tag { position: absolute; font-size: 14px; }
  .tag--before { color: var(--before); }
  .tag--after { color: var(--after-green); }
  .tag--change { color: var(--label); font-weight: 300; }
  .value { position: absolute; height: 31px; border: 1px solid var(--field-border); border-radius: 4px; background: #fff;
           font-size: 14px; line-height: 29px; text-align: center; }
  .value--before { color: var(--before); }
  .value--after { color: var(--after-green); }
  .value--change { color: #9a9a9a; font-weight: 300; }

  .section-title { position: absolute; left: 42px; top: 198px; font-size: 14px; color: var(--orange); }
  .chart-frame { position: absolute; left: 42px; top: 220px; width: 1112px; height: 541px; border: 1px solid #d0d0d0; background: #fff; }
  .chart { position: absolute; left: 42px; top: 220px; width: 1112px; height: 541px; font-family: "Carlito", Calibri, sans-serif; }
  .axis-label { font-size: 10px; fill: var(--axis-text); }
  .legend-text { font-size: 13px; fill: var(--axis-text); }
  .dl-before { font-size: 12px; font-weight: 700; fill: var(--before-text); text-anchor: middle; }
  .dl-after { font-size: 12px; font-weight: 700; fill: var(--after-text); text-anchor: middle; }
</style>
</head>
<body>
  <div class="band band--top"></div>
  <div class="band rule--top"></div>

  <span class="field-label" style="top:74px">First Name:</span>
  <div class="field" style="top:67px"></div>
  <span class="field-label" style="top:118px">Last Name:</span>
  <div class="field" style="top:113px"></div>
  <span class="field-label" style="top:164px">Age:</span>
  <div class="field" style="top:160px"></div>

  <section class="score-panel"></section>
  <span class="date" style="left:711px;top:77px">6/1/2018</span>
  <span class="date" style="left:870px;top:77px">6/16/2018</span>

  <span class="row-label" style="left:420px;width:206px;top:114px">Total Symptoms Score:</span>
  <span class="tag tag--before" style="left:634px;top:115px">Before</span>
  <div class="value value--before" style="left:691px;top:109px;width:48px">75</div>
  <span class="tag tag--after" style="left:800px;top:115px">After</span>
  <div class="value value--after" style="left:855px;top:109px;width:49px">75</div>
  <span class="tag tag--change" style="left:951px;top:115px">Change</span>
  <div class="value value--change" style="left:1021px;top:109px;width:68px">-66%</div>

  <span class="row-label" style="left:520px;width:106px;top:152px">Weight:</span>
  <span class="tag tag--before" style="left:634px;top:153px">Before</span>
  <div class="value value--before" style="left:691px;top:147px;width:51px">140</div>
  <span class="tag tag--after" style="left:800px;top:153px">After</span>
  <div class="value value--after" style="left:855px;top:147px;width:51px">140</div>
  <span class="tag tag--change" style="left:951px;top:153px">Change</span>
  <div class="value value--change" style="left:1021px;top:147px;width:70px">-9</div>

  <h2 class="section-title" style="font-weight:400">Category Symptom</h2>
  <div class="chart-frame"></div>

  <svg class="chart" viewBox="42 220 1112 541" role="img" aria-label="Area line chart of symptom scores by category, before and after">
    <g stroke="var(--grid-minor)" stroke-width="1">
      <path d="M92 717.9H1120M92 708.8H1120M92 699.7H1120M92 690.6H1120M92 672.4H1120M92 663.3H1120M92 654.2H1120M92 645.1H1120M92 626.9H1120M92 617.8H1120M92 608.7H1120M92 599.6H1120M92 581.4H1120M92 572.3H1120M92 563.2H1120M92 554.1H1120M92 535.9H1120M92 526.8H1120M92 517.7H1120M92 508.6H1120M92 490.4H1120M92 481.3H1120M92 472.2H1120M92 463.1H1120M92 444.9H1120M92 435.8H1120M92 426.7H1120M92 417.6H1120M92 399.4H1120M92 390.3H1120M92 381.2H1120M92 372.1H1120M92 353.9H1120M92 344.8H1120M92 335.7H1120M92 326.6H1120M92 308.4H1120M92 299.3H1120M92 290.2H1120M92 281.1H1120"/>
    </g>
    <g stroke="var(--grid)" stroke-width="1">
      <path d="M92 727H1120M92 681.5H1120M92 636H1120M92 590.5H1120M92 545H1120M92 499.5H1120M92 454H1120M92 408.5H1120M92 363H1120M92 317.5H1120M92 272H1120"/>
    </g>
    <g class="axis-label" text-anchor="end">
      <text x="76" y="730">0%</text><text x="76" y="685">10%</text><text x="76" y="639">20%</text>
      <text x="76" y="594">30%</text><text x="76" y="548">40%</text><text x="76" y="503">50%</text>
      <text x="76" y="457">60%</text><text x="76" y="412">70%</text><text x="76" y="366">80%</text>
      <text x="76" y="321">90%</text><text x="76" y="275">100%</text>
    </g>

    <path d="M92 727L92 672.4L171.1 586L250.2 613.2L329.2 672.4L408.3 672.4L487.4 672.4L566.5 558.6L645.6 672.4L724.6 636L803.7 522.2L882.8 272L961.9 590.5L1041 613.2L1120 708.8L1120 727Z" fill="var(--before-fill)" stroke="var(--before)" stroke-width="2"/>
    <path d="M92 727L92 672.4L171.1 727L250.2 727L329.2 727L408.3 727L487.4 699.7L566.5 727L645.6 727L724.6 704.2L803.7 681.5L882.8 658.8L961.9 704.2L1041 727L1120 727Z" fill="var(--after-fill)" stroke="var(--after)" stroke-width="2"/>

    <g class="dl-before">
      <text x="96" y="693">12%</text><text x="171" y="604">31%</text><text x="250" y="631">25%</text>
      <text x="329" y="690">12%</text><text x="408" y="690">12%</text><text x="487" y="684">12%</text>
      <text x="566" y="576">37%</text><text x="646" y="687">12%</text><text x="725" y="654">20%</text>
      <text x="811" y="541">45%</text><text x="883" y="333">100%</text><text x="957" y="608">30%</text>
      <text x="1035" y="631">25%</text><text x="1109" y="712">4%</text>
    </g>
    <g class="dl-after">
      <text x="171" y="731">0%</text><text x="250" y="731">0%</text><text x="329" y="731">0%</text>
      <text x="408" y="731">0%</text><text x="487" y="718">6%</text><text x="566" y="731">0%</text>
      <text x="646" y="731">0%</text><text x="725" y="721">5%</text><text x="804" y="700">10%</text>
      <text x="883" y="677">15%</text><text x="962" y="721">5%</text><text x="1041" y="731">0%</text>
      <text x="1120" y="731">0%</text>
    </g>

    <g class="axis-label" text-anchor="middle">
      <text x="92" y="749">Digestion</text><text x="171" y="749">Emotions</text><text x="250" y="749">Eyes</text>
      <text x="329" y="749">Lungs</text><text x="408" y="749">Mind</text><text x="487" y="749">Energy</text>
      <text x="566" y="749">Head</text><text x="646" y="749">Ears</text><text x="725" y="749">Mouth</text>
      <text x="804" y="749">Skin</text><text x="883" y="749">Pain</text><text x="962" y="749">Nose</text>
      <text x="1041" y="749">Heart</text><text x="1120" y="749">Weight</text>
    </g>

    <g>
      <rect x="546" y="237" width="9" height="9" fill="var(--before-fill)" stroke="var(--before)" stroke-width="1.5"/>
      <text class="legend-text" x="558" y="245">Before</text>
      <rect x="612" y="237" width="9" height="9" fill="var(--after-fill)" stroke="var(--after)" stroke-width="1.5"/>
      <text class="legend-text" x="624" y="245">After</text>
    </g>
  </svg>

  <div class="band rule--bottom"></div>
  <div class="band band--bottom"></div>
</body>
</html>
```